Flyer Template Design

I have attached 4 files. I would like a design template that could be used across these documents so that they have a common look and feel. The content of the documents is tested and should not be changed significantly. The images can be changed. I have also attache our logo for color compatibility.
Updates

Need extra days to review

Target Market(s)

Wealthy Christian donors

Font styles to use
Serif
Sans Serif

```html
<!DOCTYPE html>
<html lang="en">
<head>
<meta charset="utf-8">
<title>The Lastfield Fund – Finishing the Great Commission</title>
<link href="https://fonts.googleapis.com/css2?family=Tinos:wght@400;700&family=Roboto:wght@400;500&family=Nunito+Sans:wght@400;600;700&display=swap" rel="stylesheet">
<style>
  :root{
    --backdrop:#ececec;
    --paper:#ffffff;
    --navy:#0f4c81;
    --sky:#5bc4ef;
    --leaf:#9fcf7f;
    --ink:#2b2b2b;
    --band-gray:#ebebeb;
    --cta-gray:#4e4e4e;
  }
  *{margin:0;padding:0;box-sizing:border-box}
  html,body{width:1200px;height:1200px;overflow:hidden;background:var(--backdrop)}
  .flyer{position:absolute;left:142px;top:5px;width:915px;height:1190px;background:var(--paper);overflow:hidden;
    font-family:"Nunito Sans",Arial,sans-serif;color:var(--ink)}
  .masthead{position:absolute;left:0;top:0;width:915px;height:190px;background:var(--paper)}
  .brand{position:absolute;left:48px;top:78px;display:flex;align-items:center;gap:14px}
  .brand-mark{width:26px;height:26px;background:var(--navy)}
  .brand-name{font-family:"Tinos",serif;font-size:34px;line-height:34px;color:var(--navy);letter-spacing:.5px}
  .accent-rule{position:absolute;left:0;top:184px;width:915px;height:8px;background:var(--sky)}
  .accent-rule.leaf{top:176px;height:8px;background:var(--leaf)}
  .hero-photo{position:absolute;left:0;top:192px;width:915px;height:328px;
    background:linear-gradient(135deg,#6f5a4c 0%,#a47a5f 45%,#2f3c52 100%)}
  .title{position:absolute;left:48px;top:536px;font-family:"Tinos",serif;font-weight:700;font-size:30px;
    color:var(--navy);letter-spacing:.5px}
  .intro{position:absolute;left:0;top:582px;width:915px;height:89px;background:var(--band-gray);
    padding:6px 41px 0 50px;font-size:15.6px;line-height:19.3px;letter-spacing:.15px}
  .section{position:absolute;width:388px}
  .section h2{font-family:"Roboto",sans-serif;font-weight:500;font-size:23px;color:var(--navy);
    margin-bottom:7px;letter-spacing:.2px}
  .section p{font-size:14.8px;line-height:18.4px;text-align:justify}
  .marker{position:absolute;left:0;width:38px;height:26px;background:var(--navy)}
  .cta{position:absolute;left:0;top:1088px;width:915px;height:37px;background:var(--cta-gray);
    color:#fff;font-family:"Roboto",sans-serif;font-weight:500;font-size:27px;text-align:center;line-height:37px}
  .contact{position:absolute;left:0;top:1136px;width:915px;text-align:center;font-size:16px}
  .contact strong{font-weight:700}
</style>
</head>
<body>
<main class="flyer">
  <header class="masthead">
    <div class="brand">
      <span class="brand-mark"></span>
      <span class="brand-name">THE LASTFIELD FUND</span>
    </div>
  </header>
  <div class="accent-rule leaf"></div>
  <div class="accent-rule"></div>
  <div class="hero-photo" role="img" aria-label="Photo: many hands of different people clasping each other's wrists in a circle"></div>

  <h1 class="title">FINISHING THE GREAT COMMISSION</h1>

  <p class="intro">Before Jesus ascended into heaven, He commanded his apostles, “Go and make disciples of all nations.” For more than 2000 years the church has been working to fulfill this “Great Commission,” and much has been accomplished. But now, for the first time in history, our generation has the real opportunity to finish the Great Commission in our lifetimes.</p>

  <span class="marker" style="top:699px"></span>
  <section class="section" style="left:48px;top:697px">
    <h2>IT'S ABOUT NATIONS</h2>
    <p>In the Bible, the word “nations” refers to people groups: groups of people who share a common ethnicity, culture, and language. So when Jesus said, “Go and make disciples if all nations,” He was telling us to take the gospel to every people group on earth. Amazingly, there are about 12,000 of these people groups scattered throughout the world. And the Great Commission commands us to make disciples in every one of them.</p>
  </section>

  <section class="section" style="left:476px;top:699px">
    <h2>WHERE DO WE STAND?</h2>
    <p>Today, there are still about 500 people groups who have never heard the gospel. Most of these groups are small and located in remote, difficult places. These remaining “unengaged” people groups have no known believers. But now that we know who and where these groups are, by God’s grace it is possible that we can engage every one of them with the gospel within the next 3 years.</p>
  </section>

  <span class="marker" style="top:903px"></span>
  <section class="section" style="left:48px;top:901px">
    <h2>HASTENING HIS COMING</h2>
    <p>The Bible says that believers “ought to live holy and godly lives, looking for and hastening the coming of the day of God.” It also says that day will not come until the gospel has been preached to “all nations.” So how can hasten the day of his coming? By finishing the work he gave us to do: making disciples in all nations.</p>
  </section>

  <section class="section" style="left:476px;top:901px">
    <h2>YOU CAN MAKE THAT HAPPEN</h2>
    <p>Partner with the Lastfield Fund and finance the missionaries who are taking the gospel for the first time to those last remaining people groups. Your investment will “hasten the coming of the day of God” by accelerating the effort to make “disciples in every nation.” In 2018, our partners helped take the gospel to 231 people groups in 35 countries.</p>
  </section>

  <div class="cta">Join us as we invest to make disciples in “all nations” by 2022.</div>
  <p class="contact">To learn more, email Martin Hale at <strong>mhale@lastfieldfund.org.</strong></p>
</main>
</body>
</html>
```